Professional Business card

I need a business card to send with all my shipments. It needs to look very professional as I am branding myself, more than I am branding my company. The website is not active yet but that along with the instagram is very important as this will be moving shortly. The next required to be included is listed

Target Market(s)

All

Contact Information for Business Card

Very professional and sleek, I am trying to look like the CEO, motivational speaker and future president I plan to be

Colors
ffcf3e

Requirements
Must have
• Front

Derek Holmgren
CEO
Veltora Franchiser
Business Consultant/Start Up Guidance
Motivational Speaker
President of The United States 2040
www.derekholmgren-demo.com
[Instagram] @derekholmgren

Back
I teach the success method used by my company you just bought from. Learn the unique model and start your own Veltora franchise today
Nice to have
• Black and Gold lettering
Should not have
• Playful vibes

```html
<!DOCTYPE html>
<html lang="en">
<head>
<meta charset="utf-8">
<title>Derek Holmgren – Business Card</title>
<link href="https://fonts.googleapis.com/css2?family=Montserrat:wght@700&family=Quicksand:wght@400;500&display=swap" rel="stylesheet">
<style>
  :root {
    --page-bg: #0b0b0c;
    --card-bg: #0a0a0a;
    --gold-dark: #b8892f;
    --gold-mid: #d9ac52;
    --gold-light: #f0cf83;
    --gold-text: #c99d48;
    --rule-gold: #c8972f;
    --pattern-light: #151515;
    --pattern-dark: #0a0a0a;
  }
  * { margin: 0; padding: 0; box-sizing: border-box; }
  html, body {
    width: 1200px;
    height: 1200px;
    overflow: hidden;
    background: radial-gradient(circle at 50% 45%, #121214 0%, var(--page-bg) 70%);
  }
  .card {
    position: absolute;
    left: 228px;
    width: 745px;
    height: 425px;
    background: var(--card-bg);
    box-shadow: 0 18px 40px rgba(0, 0, 0, 0.55);
    overflow: hidden;
  }
  .card--front { top: 135px; }
  .card--back { top: 638px; }

  .identity__name,
  .identity__roles,
  .identity__rule,
  .identity__links {
    position: absolute;
    left: 169px;
    width: 405px;
  }
  .identity__name {
    top: 114px;
    height: 40px;
    overflow: visible;
    filter: drop-shadow(0 2px 2px rgba(0, 0, 0, 0.9));
  }
  .identity__name text {
    font-family: "Montserrat", sans-serif;
    font-weight: 700;
    font-size: 30px;
  }
  .identity__roles {
    top: 163px;
    height: 92px;
    overflow: visible;
    filter: drop-shadow(0 1px 1px rgba(0, 0, 0, 0.9));
  }
  .identity__roles text {
    font-family: "Quicksand", sans-serif;
    font-weight: 400;
    font-size: 18.5px;
    fill: var(--gold-text);
  }
  .identity__rule {
    top: 268px;
    height: 1.5px;
    background: var(--rule-gold);
  }
  .identity__links {
    top: 286px;
    height: 22px;
    display: flex;
    justify-content: space-between;
    align-items: center;
    font-family: "Quicksand", sans-serif;
    font-size: 15px;
    color: var(--gold-text);
    white-space: nowrap;
  }
  .identity__social {
    display: flex;
    align-items: center;
    gap: 7px;
  }
  .identity__dot {
    width: 17px;
    height: 17px;
    border-radius: 50%;
    background: var(--gold-mid);
  }

  .back__pattern {
    position: absolute;
    inset: 0;
    background: linear-gradient(160deg, var(--pattern-light) 0%, var(--pattern-dark) 40%, var(--pattern-light) 75%, var(--pattern-dark) 100%);
  }
  .back__pitch {
    position: absolute;
    left: 28px;
    top: 180px;
    width: 692px;
    height: 56px;
    overflow: visible;
    filter: drop-shadow(0 2px 2px rgba(0, 0, 0, 0.95));
  }
  .back__pitch text {
    font-family: "Quicksand", sans-serif;
    font-weight: 500;
    font-size: 19.5px;
    fill: var(--gold-mid);
  }
</style>
</head>
<body>
  <section class="card card--front">
    <svg class="identity__name" viewBox="0 0 405 40" aria-label="Derek Holmgren - CEO">
      <defs>
        <linearGradient id="name-gold" x1="0" y1="0" x2="0" y2="1">
          <stop offset="0" stop-color="#f0cf83"/>
          <stop offset="0.5" stop-color="#d9ac52"/>
          <stop offset="1" stop-color="#b8892f"/>
        </linearGradient>
      </defs>
      <text x="0" y="31" fill="url(#name-gold)" textLength="405" lengthAdjust="spacingAndGlyphs">DEREK HOLMGREN - CEO</text>
    </svg>
    <svg class="identity__roles" viewBox="0 0 405 92">
      <text x="0" y="25" textLength="405" lengthAdjust="spacing">Veltora Franchiser - Motivational Speaker</text>
      <text x="0" y="54" textLength="405" lengthAdjust="spacing">Business Consultant/Start Up Guidance</text>
      <text x="0" y="84" textLength="405" lengthAdjust="spacing">President of The United States 2040</text>
    </svg>
    <div class="identity__rule"></div>
    <div class="identity__links">
      <span class="identity__web">www.derekholmgren-demo.com</span>
      <span class="identity__social"><span class="identity__dot"></span>@derekholmgren</span>
    </div>
  </section>

  <section class="card card--back">
    <div class="back__pattern" role="img" aria-label="Faint diagonal repeated name pattern in dark grey"></div>
    <svg class="back__pitch" viewBox="0 0 692 56">
      <text x="0" y="24" textLength="690" lengthAdjust="spacing">I teach the success method used by my compan you just bought from.</text>
      <text x="0" y="49" textLength="692" lengthAdjust="spacing">Learn the unique model and start your own Veltora franchise today</text>
    </svg>
  </section>
</body>
</html>
```